Branded Powerpoint Slide update

Design a clean, modern, professional corporate powerpoint template that include the Brightwell Corporation word-mark logo, brand color, and brand font. The design should come with a variety of sample pages - I have attached a Template sample of what the template should include. I have also included a sample slide that contains newly created brand elements. Feel free to use this as a guide.
Templates should be produced in A4 and Letter formats as a powerpoint file and should use Helvetica Now Display as the embedded font.
Design Preferences:
Cover should stand alone with engaging elements. Overall, design elements should remain minimal as to not dominate the slide. Colour block designs, solid borders with flowing smooth lines, single side borders with connected header and footer, cut off or half page headers and footers are all acceptable.
Enclosed are:
1. Three word mark logos with reverse versions of each, one for each primary brand colour. ('b-invert, o-invert, 0-main, b-main)
2. Brightwell corporate colour pallet (brightwell brand... )
3. Helvetica Now Display font files
4. Sample of Powerpoint template to show types of pages needed for inclusion ('Sample Slide Deck.ppt)
5. Sample of newly created brand elements for simple Header/Text Body slide. (both 'letterhead...ai" files are the raw files. 'Powerpoint slide Template Sample' is the sample being used).
Technology Equipment

```html
<!DOCTYPE html>
<html lang="en">
<head>
<meta charset="utf-8">
<title>Brightwell Slide Template</title>
<link href="https://fonts.googleapis.com/css2?family=Archivo:wght@800;900&family=Roboto:wght@400;500;700&display=swap" rel="stylesheet">
<style>
:root{
  --navy:#161b2b;
  --blue:#1a9ff0;
  --red:#f52a0a;
  --ink:#1d2233;
  --muted:#6b6f78;
  --page:#c8c8c8;
  --white:#ffffff;
}
*{box-sizing:border-box;margin:0;padding:0}
html,body{width:1200px;height:4255px;overflow:hidden}
body{background:var(--page);font-family:"Roboto",Arial,sans-serif;color:var(--ink);position:relative}
.slide{position:absolute;left:121px;width:958px;height:580px;background:var(--white);overflow:hidden}

/* cover */
.cover{top:160px;background:var(--navy)}
.cover-title{position:absolute;left:31px;top:80px;color:var(--white);font-family:"Archivo",Arial,sans-serif;font-weight:900;font-size:40px;line-height:1.18;letter-spacing:.5px}
.cover-sub{position:absolute;left:31px;top:210px;width:420px;color:#e8eaf0;font-size:16.5px;line-height:1.8}
.cover-photo{position:absolute;left:544px;top:55px;width:386px;height:386px;border-radius:50%;background:radial-gradient(circle at 40% 40%,#c9c4bd,#7b7f86 60%,#3b3f48)}
.cover-wave{position:absolute;left:0;top:0}
.cover-brand{position:absolute;left:31px;top:465px;color:var(--red);font-family:"Archivo",Arial,sans-serif;font-weight:900;font-size:56px;letter-spacing:-1px}
.social{position:absolute;top:510px;display:flex;gap:10px;left:749px}
.social span{width:36px;height:36px;border:2.5px solid var(--navy);border-radius:50%}
.cover-rule{position:absolute;left:0;bottom:0;width:100%;height:6px;background:var(--blue)}

/* inner slides */
.slide-head{position:absolute;left:0;top:0;width:100%;height:63px}
.slide-title{position:absolute;left:39px;top:14px;color:var(--white);font-family:"Archivo",Arial,sans-serif;font-weight:800;font-size:28px;letter-spacing:.2px}
.page-num{position:absolute;right:18px;top:20px;color:var(--white);font-size:17px}
.side-rule{position:absolute;left:39px;top:63px;width:1.5px;height:480px;background:#e2e2e2}
.foot-rule{position:absolute;left:0;bottom:18px;width:100%;height:12px;background:var(--red)}
.foot-line{position:absolute;left:0;bottom:8px;width:100%;height:3px;background:var(--navy)}
.foot-brand{position:absolute;left:38px;bottom:10px;padding:0 6px 0 2px;background:var(--white);color:var(--blue);font-family:"Archivo",Arial,sans-serif;font-weight:900;font-size:37px;line-height:1}

/* team */
.member{position:absolute;top:145px;width:290px;text-align:center}
.avatar{width:156px;height:156px;margin:0 auto;border-radius:50%;border:4px solid #fff;box-shadow:0 0 0 2px #d6d6d6,0 4px 10px rgba(0,0,0,.15)}
.member-name{margin-top:22px;font-size:19px;font-weight:500;color:var(--ink)}
.member-role{margin-top:6px;font-size:14.5px;color:var(--muted)}
.member-bio{margin-top:12px;font-size:15px;line-height:1.72;color:#4b4f59}

/* cycle */
.cycle-item{position:absolute;width:260px;font-size:11.5px;line-height:1.55;color:#4b4f59}
.cycle-item h3{font-size:15px;font-weight:700;color:var(--ink);margin-bottom:14px}
.cycle-item.left{text-align:right}

/* cards */
.card{position:absolute;top:168px;width:250px;height:293px;border-radius:14px;background:var(--white);box-shadow:0 6px 18px rgba(0,0,0,.12);text-align:center;padding-top:28px}
.card h3{margin-top:12px;font-size:19px;font-weight:500;color:#1b6fc0}
.card p{margin:22px 16px 0;font-size:15px;line-height:1.72;color:var(--muted)}

/* features */
.feature{position:absolute;left:54px;width:480px}
.feature-icon{position:absolute;left:0;top:4px;width:86px;height:86px;border-radius:50%}
.feature h3{margin-left:108px;font-size:18px;font-weight:500;color:var(--ink)}
.feature p{margin:16px 0 0 108px;width:360px;font-size:16px;line-height:1.62;color:#5a5e67}
.device-photo{position:absolute;left:520px;top:160px;width:400px;height:310px;border-radius:10px;background:linear-gradient(135deg,#e4e6e8,#a3a9b0 55%,#5d636b)}
</style>
</head>
<body>

<!-- Cover -->
<section class="slide cover">
  <div class="cover-photo" role="img" aria-label="Photo of a smiling business team gathered around a meeting table"></div>
  <svg class="cover-wave" width="958" height="580" viewBox="0 0 958 580">
    <path d="M0 448 C140 340 330 400 520 470 C700 530 860 470 958 430 L958 580 L0 580Z" fill="var(--red)"/>
    <path d="M0 470 C140 368 330 420 520 488 C700 548 860 492 958 455 L958 580 L0 580Z" fill="var(--white)"/>
  </svg>
  <h1 class="cover-title">PRESENTATION<br>TITLE HERE</h1>
  <p class="cover-sub">Sed ut perspiciatis unde omnis iste voluptatem accusantium doloremque laudantium, totam rem aperiam, eaque ipsa quae</p>
  <div class="cover-brand">Brightwell</div>
  <div class="social"><span></span><span></span><span></span><span></span></div>
  <div class="cover-rule"></div>
</section>

<!-- Team -->
<section class="slide" style="top:830px">
  <svg class="slide-head" width="958" height="63"><rect width="958" height="63" fill="var(--red)"/><polygon points="0,0 588,0 575,63 0,63" fill="var(--navy)"/><polygon points="592,0 845,0 832,63 579,63" fill="var(--blue)"/></svg>
  <h2 class="slide-title">TEAM PRESENTATION</h2><span class="page-num">Page: 01</span>
  <div class="side-rule"></div>
  <div class="member" style="left:33px"><div class="avatar" role="img" aria-label="Portrait of Amara Okoye" style="background:linear-gradient(160deg,#a9583f,#e8603a)"></div><div class="member-name">Amara Okoye</div><div class="member-role">Job Title</div><p class="member-bio">Lorem ipsum dolor sit consectetur adipiscing elit, do eiusmod tempor incididunt ut labore et dolore</p></div>
  <div class="member" style="left:340px"><div class="avatar" role="img" aria-label="Portrait of Mateo Ruiz" style="background:linear-gradient(160deg,#3a3a3a,#1d1d1d)"></div><div class="member-name">Mateo Ruiz</div><div class="member-role">Job Title</div><p class="member-bio">Lorem ipsum dolor sit consectetur adipiscing elit, do eiusmod tempor incididunt ut labore et dolore</p></div>
  <div class="member" style="left:647px"><div class="avatar" role="img" aria-label="Portrait of Lucia Moreno" style="background:linear-gradient(160deg,#b9bcc0,#8a6a5e)"></div><div class="member-name">Lucia Moreno</div><div class="member-role">Job Title</div><p class="member-bio">Lorem ipsum dolor sit consectetur adipiscing elit, do eiusmod tempor incididunt ut labore et dolore</p></div>
  <div class="foot-line"></div><div class="foot-rule"></div><div class="foot-brand">Brightwell</div>
</section>

<!-- Cycle -->
<section class="slide" style="top:1500px">
  <svg class="slide-head" width="958" height="63"><rect width="958" height="63" fill="var(--red)"/><polygon points="0,0 588,0 575,63 0,63" fill="var(--navy)"/><polygon points="592,0 845,0 832,63 579,63" fill="var(--blue)"/></svg>
  <h2 class="slide-title">TEAM PRESENTATION</h2><span class="page-num">Page: 02</span>
  <div class="side-rule"></div>
  <svg style="position:absolute;left:322px;top:137px" width="320" height="320" viewBox="-160 -160 320 320">
    <g fill="none" stroke-width="66">
      <circle r="123" stroke="var(--red)" stroke-dasharray="120 653" transform="rotate(-150)"/>
      <circle r="123" stroke="var(--blue)" stroke-dasharray="120 653" transform="rotate(-88)"/>
      <circle r="123" stroke="var(--red)" stroke-dasharray="120 653" transform="rotate(-28)"/>
      <circle r="123" stroke="var(--blue)" stroke-dasharray="120 653" transform="rotate(32)"/>
      <circle r="123" stroke="var(--red)" stroke-dasharray="120 653" transform="rotate(92)"/>
      <circle r="123" stroke="var(--blue)" stroke-dasharray="120 653" transform="rotate(152)"/>
    </g>
    <g fill="var(--white)">
      <circle cx="-62" cy="-106" r="10"/><circle cx="58" cy="-106" r="10"/><circle cx="120" cy="0" r="10"/>
      <circle cx="60" cy="106" r="10"/><circle cx="-60" cy="106" r="10"/><circle cx="-120" cy="0" r="10"/>
    </g>
    <text y="12" text-anchor="middle" font-family="Archivo, Arial, sans-serif" font-weight="900" font-size="32" fill="var(--red)">Brightwell</text>
  </svg>
  <div class="cycle-item left" style="left:73px;top:125px"><h3>Lorem ipsum dolor</h3>Lorem ipsum dolor sit amet, consectetur adipiscing elit, sed do eiusmod tempor</div>
  <div class="cycle-item left" style="left:23px;top:260px"><h3>Lorem ipsum dolor</h3>Lorem ipsum dolor sit amet, consectetur adipiscing elit, sed do eiusmod tempor</div>
  <div class="cycle-item left" style="left:82px;top:395px"><h3>Lorem ipsum dolor</h3>Lorem ipsum dolor sit amet, consectetur adipiscing elit, sed do eiusmod tempor</div>
  <div class="cycle-item" style="left:623px;top:125px"><h3>Lorem ipsum dolor</h3>Lorem ipsum dolor sit amet, consectetur adipiscing elit, sed do eiusmod tempor</div>
  <div class="cycle-item" style="left:679px;top:260px"><h3>Lorem ipsum dolor</h3>Lorem ipsum dolor sit amet, consectetur adipiscing elit, sed do eiusmod tempor</div>
  <div class="cycle-item" style="left:630px;top:395px"><h3>Lorem ipsum dolor</h3>Lorem ipsum dolor sit amet, consectetur adipiscing elit, sed do eiusmod tempor</div>
  <div class="foot-line"></div><div class="foot-rule"></div><div class="foot-brand">Brightwell</div>
</section>

<!-- Chart -->
<section class="slide" style="top:2170px">
  <svg class="slide-head" width="958" height="63"><rect width="958" height="63" fill="var(--red)"/><polygon points="0,0 588,0 575,63 0,63" fill="var(--navy)"/><polygon points="592,0 845,0 832,63 579,63" fill="var(--blue)"/></svg>
  <h2 class="slide-title">OUR AWESOME TITLE</h2><span class="page-num">Page: 03</span>
  <div class="side-rule"></div>
  <svg style="position:absolute;left:0;top:0" width="958" height="520" font-family="Roboto, Arial, sans-serif">
    <g stroke="#e3e3e3" stroke-width="1"><line x1="142" y1="152" x2="885" y2="152"/><line x1="142" y1="222" x2="885" y2="222"/><line x1="142" y1="292" x2="885" y2="292"/><line x1="142" y1="362" x2="885" y2="362"/><line x1="142" y1="432" x2="885" y2="432"/></g>
    <g font-size="19" fill="#333" text-anchor="end"><text x="128" y="159">40</text><text x="128" y="229">30</text><text x="128" y="299">20</text><text x="128" y="369">10</text><text x="128" y="439">0</text></g>
    <g>
      <rect x="195" y="236" width="25" height="196" fill="var(--blue)"/><rect x="226" y="222" width="25" height="210" fill="var(--navy)"/><rect x="257" y="250" width="25" height="182" fill="var(--red)"/>
      <rect x="380" y="208" width="25" height="224" fill="var(--blue)"/><rect x="411" y="236" width="25" height="196" fill="var(--navy)"/><rect x="442" y="257" width="25" height="175" fill="var(--red)"/>
      <rect x="566" y="152" width="25" height="280" fill="var(--blue)"/><rect x="597" y="250" width="25" height="182" fill="var(--navy)"/><rect x="628" y="306" width="25" height="126" fill="var(--red)"/>
      <rect x="751" y="171" width="25" height="261" fill="var(--blue)"/><rect x="782" y="285" width="25" height="147" fill="var(--navy)"/><rect x="813" y="271" width="25" height="161" fill="var(--red)"/>
    </g>
    <g font-size="20" font-weight="700" fill="#222" text-anchor="middle"><text x="238" y="468">2015</text><text x="423" y="468">2016</text><text x="609" y="468">2017</text><text x="794" y="468">2018</text></g>
  </svg>
  <div class="foot-line"></div><div class="foot-rule"></div><div class="foot-brand">Brightwell</div>
</section>

<!-- Cards -->
<section class="slide" style="top:2840px">
  <svg class="slide-head" width="958" height="63"><rect width="958" height="63" fill="var(--red)"/><polygon points="0,0 588,0 575,63 0,63" fill="var(--navy)"/><polygon points="592,0 845,0 832,63 579,63" fill="var(--blue)"/></svg>
  <h2 class="slide-title">OUR AWESOME TITLE</h2><span class="page-num">Page: 04</span>
  <div class="side-rule"></div>
  <div class="card" style="left:54px">
    <svg width="50" height="50" viewBox="0 0 50 50"><circle cx="25" cy="27" r="20" fill="var(--blue)"/><circle cx="25" cy="27" r="12" fill="#fff"/><circle cx="25" cy="27" r="6" fill="var(--red)"/><line x1="25" y1="27" x2="12" y2="6" stroke="var(--red)" stroke-width="3"/></svg>
    <h3>Lorem ipsum dolor</h3><p>Sed perspiciatis unde omnis iste natus error sit voluptatem accusantium doloremque laudantium, totam rem aperiam, eaque ipsa</p>
  </div>
  <div class="card" style="left:355px">
    <svg width="50" height="50" viewBox="0 0 50 50"><rect x="14" y="8" width="28" height="12" rx="3" fill="var(--blue)" transform="rotate(-20 28 14)"/><rect x="4" y="14" width="10" height="8" fill="var(--red)" transform="rotate(-20 9 18)"/><line x1="25" y1="22" x2="14" y2="46" stroke="var(--blue)" stroke-width="3"/><line x1="25" y1="22" x2="36" y2="46" stroke="var(--blue)" stroke-width="3"/><line x1="25" y1="22" x2="25" y2="46" stroke="var(--blue)" stroke-width="3"/></svg>
    <h3>Lorem ipsum dolor</h3><p>Sed perspiciatis unde omnis iste natus error sit voluptatem accusantium doloremque laudantium, totam rem aperiam, eaque ipsa</p>
  </div>
  <div class="card" style="left:655px">
    <svg width="50" height="50" viewBox="0 0 50 50"><rect x="8" y="34" width="8" height="12" fill="var(--blue)"/><rect x="19" y="28" width="8" height="18" fill="var(--blue)"/><rect x="30" y="20" width="8" height="26" fill="var(--blue)"/><line x1="8" y1="26" x2="30" y2="10" stroke="var(--red)" stroke-width="3"/><line x1="38" y1="4" x2="38" y2="18" stroke="var(--red)" stroke-width="2"/><polygon points="38,4 48,7 38,11" fill="var(--red)"/></svg>
    <h3>Lorem ipsum dolor</h3><p>Sed perspiciatis unde omnis iste natus error sit voluptatem accusantium doloremque laudantium, totam rem aperiam, eaque ipsa</p>
  </div>
  <div class="foot-line"></div><div class="foot-rule"></div><div class="foot-brand">Brightwell</div>
</section>

<!-- Features -->
<section class="slide" style="top:3510px">
  <svg class="slide-head" width="958" height="63"><rect width="958" height="63" fill="var(--red)"/><polygon points="0,0 588,0 575,63 0,63" fill="var(--navy)"/><polygon points="592,0 845,0 832,63 579,63" fill="var(--blue)"/></svg>
  <h2 class="slide-title">OUR AWESOME TITLE</h2><span class="page-num">Page: 05</span>
  <div class="side-rule"></div>
  <div class="feature" style="top:164px">
    <div class="feature-icon" style="background:var(--blue)"><svg width="86" height="86" viewBox="0 0 86 86" fill="none" stroke="#fff" stroke-width="2.5"><rect x="26" y="30" width="22" height="6"/><rect x="26" y="38" width="22" height="6"/><rect x="26" y="46" width="22" height="6"/><circle cx="54" cy="50" r="10"/></svg></div>
    <h3>Lorem ipsum dolor sit amet</h3><p>Sed ut perspiciatis unde omnis iste natus error voluptatem accusantium doloremque enim laudantium,</p>
  </div>
  <div class="feature" style="top:334px">
    <div class="feature-icon" style="background:var(--red)"><svg width="86" height="86" viewBox="0 0 86 86" fill="none" stroke="#fff" stroke-width="2.5"><rect x="28" y="24" width="26" height="36" rx="2"/><line x1="33" y1="34" x2="49" y2="34"/><line x1="33" y1="41" x2="49" y2="41"/><line x1="33" y1="48" x2="45" y2="48"/><line x1="60" y1="30" x2="60" y2="58"/></svg></div>
    <h3>Lorem ipsum dolor sit amet</h3><p>Sed ut perspiciatis unde omnis iste natus error voluptatem accusantium doloremque enim laudantium,</p>
  </div>
  <div class="device-photo" role="img" aria-label="Photo of a tablet displaying a team meeting"></div>
  <div class="foot-line"></div><div class="foot-rule"></div><div class="foot-brand">Brightwell</div>
</section>

</body>
</html>
```